Business Landing Page for SEO Company

Need the landing page of the website designed - I will provide the copy, will need to include details of my company and the services offered, about us, testimonials, faq, etc., and all these elements will need to be arranged graphically on the page.

I want something similar to this: https://plorvantix.com/

Not in terms of color or theme or anything, but we offer a similar service and want to display similar information.

Th services we provide are:

Premium Links
Monthly Links Subscription
Link Insertions

Need to advertise them on the front page. Additionally need a place for testimonials, company details, etc.,

We already have logo for the website. Please use the attached file to insert the logo within the overal design.
Updates

Target Market(s)

SEO marketers and agencies

Number of Pages Required

1 page

```html
<!DOCTYPE html>
<html lang="en">
<head>
<meta charset="utf-8">
<title>Tallvine – SEO Management</title>
<link href="https://fonts.googleapis.com/css2?family=Lexend:wght@400;500;600&family=Montserrat:wght@400;500;600&display=swap" rel="stylesheet">
<style>
:root{
  --blue:#2f8de4;
  --orange:#ff8a00;
  --cyan:#00f2f6;
  --ink:#1c1c1c;
  --muted:#6f6f6f;
  --tint:#f2f8fd;
  --foot:#ededed;
  --white:#ffffff;
  --line:#e6e6e6;
}
*{box-sizing:border-box;margin:0;padding:0}
html,body{width:1200px;height:4225px;overflow:hidden}
body{position:relative;background:var(--white);font-family:"Montserrat",sans-serif;color:var(--ink)}
.abs{position:absolute}
.head{font-family:"Lexend",sans-serif;font-weight:500}
.eyebrow{font-family:"Lexend",sans-serif;font-weight:500;color:var(--blue);font-size:18px;letter-spacing:2px}
.accent{color:var(--orange)}
.blue{color:var(--blue)}
.center{left:0;width:1200px;text-align:center}
.brand{font-family:"Lexend",sans-serif;font-weight:600;color:var(--blue);font-size:34px;display:flex;align-items:center;gap:8px}
.brand i{display:block;width:12px;height:12px;border-radius:50%;background:var(--orange)}
.nav a{position:absolute;top:26px;font-size:13px;color:var(--ink);text-decoration:none}
.btn{position:absolute;display:flex;align-items:center;justify-content:center;border-radius:30px;font-size:12px;font-weight:600;font-family:"Montserrat",sans-serif}
.btn-solid{background:var(--orange);color:var(--white)}
.btn-ghost{border:1.5px solid var(--orange);color:var(--orange)}
.btn-dark{border:1.5px solid #555;color:var(--ink);font-weight:500}
.para{font-size:13.5px;line-height:22.5px;color:#444}
.band-tint{left:0;width:1200px;background:var(--tint)}
.service .ic{width:82px;height:82px;border-radius:50%;background:var(--white);box-shadow:0 8px 22px rgba(47,141,228,.12);display:flex;align-items:center;justify-content:center}
.service h3{font-family:"Lexend",sans-serif;font-weight:500;font-size:21px;margin-top:42px;white-space:nowrap}
.service p{font-size:13.5px;line-height:22px;color:var(--muted);margin-top:18px;width:240px}
.plan{top:2100px;width:258px;height:364px;background:var(--white);box-shadow:0 6px 30px rgba(0,0,0,.06);text-align:center;padding-top:36px}
.plan h4{font-family:"Lexend",sans-serif;font-weight:400;font-size:18px;color:#555}
.plan .price{font-family:"Lexend",sans-serif;font-weight:500;font-size:22px;color:var(--blue);margin-top:12px}
.plan ul{list-style:none;margin-top:16px}
.plan li{font-size:13.5px;line-height:33px;color:var(--ink)}
.plan .buy{display:inline-flex;align-items:center;justify-content:center;width:100px;height:30px;border:1.5px solid #555;border-radius:20px;font-size:11px;margin-top:18px}
.plan.featured{background:var(--blue)}
.plan.featured h4,.plan.featured .price,.plan.featured li{color:var(--white)}
.plan.featured .buy{background:var(--white);border-color:var(--white);color:var(--ink)}
.quote{top:2634px;width:261px;height:336px;background:var(--white);box-shadow:0 6px 26px rgba(0,0,0,.05);padding:40px 34px 0}
.quote .stars{color:#f5b400;font-size:14px;letter-spacing:1px}
.quote p{font-size:13.5px;line-height:22.5px;color:#444;margin-top:14px}
.quote .who{display:flex;align-items:center;gap:12px;margin-top:24px}
.quote .av{width:40px;height:40px;border-radius:50%;background:linear-gradient(135deg,#c9d3dc,#8d9aa6)}
.quote b{font-family:"Lexend",sans-serif;font-weight:500;font-size:13.5px;display:block}
.quote small{font-size:10px;color:#999}
.faq{font-size:13.5px;font-weight:600;font-family:"Montserrat",sans-serif}
.faq .sign{position:absolute;color:var(--orange);font-weight:500;font-size:18px}
.foot-col h5{font-family:"Lexend",sans-serif;font-weight:500;font-size:14px}
.foot-col a{position:absolute;left:0;font-size:12px;color:var(--ink);text-decoration:none}
</style>
</head>
<body>

<!-- Hero backdrop -->
<svg class="abs" style="left:0;top:0" width="1200" height="620" aria-hidden="true">
  <polygon points="800,0 1200,0 1200,385 1010,495 600,345" fill="var(--cyan)"/>
</svg>

<!-- Header -->
<header>
  <div class="abs brand" style="left:188px;top:10px"><i></i>Tallvine</div>
  <nav class="nav">
    <a style="left:398px">Home</a>
    <a style="left:470px">About us</a>
    <a style="left:561px">Service</a>
    <a style="left:641px">Testimonials</a>
    <a style="left:751px">Contact us</a>
  </nav>
  <a class="btn btn-solid" style="left:905px;top:16px;width:106px;height:38px">Get a Quote</a>
</header>

<!-- Hero -->
<section>
  <div class="abs eyebrow" style="left:188px;top:164px">SEO MANAGEMENT</div>
  <h1 class="abs head" style="left:188px;top:205px;font-size:42px;line-height:50px;font-weight:500">In-Depth Busniess<br><span class="accent">SEO Solution</span></h1>
  <p class="abs" style="left:188px;top:330px;font-size:15px;line-height:23px;color:#444;width:340px">Lorem ipsum dolor sit amet consectetur adipiscing elit sed do eiusmod.</p>
  <a class="btn btn-dark" style="left:188px;top:410px;width:122px;height:41px">Get Started</a>
  <div class="abs" role="img" aria-label="Illustration of two people arranging charts on a large dashboard screen with gears" style="left:600px;top:170px;width:430px;height:390px;border-radius:50%;background:radial-gradient(circle at 50% 55%,#dff5ef 0%,#eeeeee 55%,#f3f3f3 100%)"></div>
</section>

<!-- Trusted -->
<section>
  <p class="abs center head" style="top:630px;font-size:21px;font-weight:500">Trusted by over <span class="blue">35,000</span> companies</p>
  <div class="abs" style="left:192px;top:696px;width:112px;height:24px;border-radius:6px;background:#dcdcdc"></div>
  <div class="abs" style="left:390px;top:696px;width:76px;height:24px;border-radius:6px;background:#dcdcdc"></div>
  <div class="abs" style="left:546px;top:696px;width:120px;height:24px;border-radius:6px;background:#dcdcdc"></div>
  <div class="abs" style="left:734px;top:696px;width:102px;height:24px;border-radius:6px;background:#dcdcdc"></div>
  <div class="abs" style="left:913px;top:696px;width:100px;height:24px;border-radius:6px;background:#dcdcdc"></div>
  <div class="abs" style="left:188px;top:777px;width:832px;height:1px;background:var(--line)"></div>
</section>

<!-- About -->
<section>
  <div class="abs" role="img" aria-label="Illustration of a person with a tablet beside a large monitor showing analytics and a magnifying glass" style="left:184px;top:852px;width:367px;height:369px;border-radius:50% 50% 50% 50%/58% 58% 42% 42%;background:radial-gradient(circle at 45% 45%,#dff5ef 0%,#e9e9e9 60%,#efefef 100%)"></div>
  <div class="abs eyebrow" style="left:615px;top:850px">ABOUT US</div>
  <h2 class="abs head" style="left:615px;top:888px;font-size:29px;line-height:39px">We Are The Best<br><span class="accent">SEO Company</span></h2>
  <p class="abs para" style="left:615px;top:976px;width:340px">Lorem ipsum dolor sit amet, consectetur adipiscing elit, sed do eiusmod tempor incididunt ut labore et dolore magna aliqua. Ut enim ad minim veniam, quis nostrud exercitation ullamco laboris nisi ut aliquip ex ea commodo consequat. Duis aute irure dolor in reprehenderit in voluptate velit esse cillum dolore.</p>
  <a class="btn btn-ghost" style="left:615px;top:1160px;width:131px;height:45px;font-size:11px">More About us</a>
</section>

<!-- Services -->
<section>
  <div class="abs band-tint" style="top:1292px;height:618px"></div>
  <div class="abs center eyebrow" style="top:1352px">OUR SERVICES</div>
  <h2 class="abs center head" style="top:1390px;font-size:29px;line-height:39px">We Provide<br><span class="accent">Professional Range Services</span></h2>

  <div class="abs service" style="left:198px;top:1508px">
    <div class="ic"><svg width="40" height="40" viewBox="0 0 40 40" fill="none" stroke="var(--blue)" stroke-width="2.4"><rect x="4" y="8" width="26" height="18" rx="3"/><path d="M12 32h12M18 26v6"/><circle cx="28" cy="12" r="7" fill="var(--orange)" stroke="none"/></svg></div>
    <h3>SEO Counsulting</h3>
    <p>Lorem ipsum dolor sit amet conse ctetur adipiscing elit sedei usm od tempor.</p>
  </div>
  <div class="abs service" style="left:469px;top:1508px">
    <div class="ic"><svg width="40" height="40" viewBox="0 0 40 40" fill="none" stroke="var(--blue)" stroke-width="2.4"><path d="M11 26a7 7 0 0 1 1-14 9 9 0 0 1 17 3 6 6 0 0 1 0 11"/><circle cx="21" cy="26" r="5" stroke="var(--orange)"/><path d="M25 30l4 4" stroke="var(--orange)"/></svg></div>
    <h3>Content Optimization</h3>
    <p>Lorem ipsum dolor sit amet conse ctetur adipiscing elit sedei usm od tempor.</p>
  </div>
  <div class="abs service" style="left:752px;top:1508px">
    <div class="ic"><svg width="40" height="40" viewBox="0 0 40 40" fill="none" stroke="var(--blue)" stroke-width="2.4"><rect x="6" y="22" width="6" height="12" rx="3"/><rect x="17" y="18" width="6" height="16" rx="3"/><rect x="28" y="14" width="6" height="20" rx="3"/><path d="M6 14l8-6 6 4 12-8M28 4h4v4" stroke="var(--orange)"/></svg></div>
    <h3>Seo Stategy</h3>
    <p>Lorem ipsum dolor sit amet conse ctetur adipiscing elit sedei usm od tempor.</p>
  </div>
  <a class="btn btn-solid" style="left:533px;top:1778px;width:134px;height:46px;font-size:12px">View More</a>
</section>

<!-- Pricing -->
<section>
  <div class="abs center eyebrow" style="top:1978px">PRICE</div>
  <h2 class="abs center head" style="top:2014px;font-size:29px">Reasonable <span class="accent">Pricing</span></h2>
  <div class="abs plan" style="left:188px">
    <h4>Premium</h4><div class="price">$99.00</div>
    <ul><li>Analystic Campaign</li><li>1500 KeyWords</li><li>25 social Media Reviews</li><li>1 Free Optimization</li><li>24/7 Supports</li></ul>
    <span class="buy">Buy Now!</span>
  </div>
  <div class="abs plan featured" style="left:470px;width:259px">
    <h4>Monthly</h4><div class="price">$199.00</div>
    <ul><li>Analystic Campaign</li><li>1500 KeyWords</li><li>25 social Media Reviews</li><li>1 Free Optimization</li><li>24/7 Supports</li></ul>
    <span class="buy">Buy Now!</span>
  </div>
  <div class="abs plan" style="left:752px">
    <h4>Subscription</h4><div class="price">$150.00</div>
    <ul><li>Analystic Campaign</li><li>1500 KeyWords</li><li>25 social Media Reviews</li><li>1 Free Optimization</li><li>24/7 Supports</li></ul>
    <span class="buy">Buy Now</span>
  </div>
</section>

<!-- Feedback -->
<section>
  <div class="abs" style="left:0;top:2541px;width:1200px;height:470px;background:linear-gradient(180deg,var(--tint) 0%,var(--white) 100%)"></div>
  <div class="abs eyebrow" style="left:188px;top:2634px">FEEDBACK</div>
  <h2 class="abs head" style="left:188px;top:2669px;font-size:28px;line-height:38px">Clients Give Us<br><span class="accent">Excellent Quotes</span></h2>
  <p class="abs para" style="left:188px;top:2759px;width:245px">Lorem ipsum dolor sit amet conse ctetur adipiscing elit sed do eius mod tempor incididunt ut labore et dolore magna aliqua.</p>
  <div class="abs" style="left:188px;top:2890px;width:37px;height:37px;border-radius:50%;background:var(--white);box-shadow:0 4px 12px rgba(0,0,0,.08);display:flex;align-items:center;justify-content:center"><svg width="10" height="12" viewBox="0 0 10 12"><path d="M7 1L2 6l5 5" fill="none" stroke="#999" stroke-width="1.6"/></svg></div>
  <div class="abs" style="left:240px;top:2890px;width:37px;height:37px;border-radius:50%;background:var(--orange);display:flex;align-items:center;justify-content:center"><svg width="10" height="12" viewBox="0 0 10 12"><path d="M3 1l5 5-5 5" fill="none" stroke="#fff" stroke-width="1.6"/></svg></div>

  <div class="abs quote" style="left:470px">
    <div class="stars">★★★★☆</div>
    <p>sed do eiusmod tempor incididunt ut labore et dolore magna aliqua. Ut enim ad minim veniam, quis nostrud exercitation ullamco laboris nisi ut aliquip ex eammodo consequatDuis aute.</p>
    <div class="who"><div class="av" role="img" aria-label="Client portrait"></div><div><b>John Doe</b><small>Happy People</small></div></div>
  </div>
  <div class="abs quote" style="left:751px">
    <div class="stars">★★★★☆</div>
    <p>sed do eiusmod tempor incididunt ut labore et dolore magna aliqua. Ut enim ad minim veniam, quis nostrud exercitation ullamco laboris nisi ut aliquip ex eammodo consequatDuis aute.</p>
    <div class="who"><div class="av" role="img" aria-label="Client portrait"></div><div><b>John Doe</b><small>Happy People</small></div></div>
  </div>
</section>

<!-- FAQ -->
<section class="faq">
  <div class="abs center eyebrow" style="top:3066px">FAQ</div>
  <h2 class="abs center head" style="top:3102px;font-size:29px">Have Any <span class="accent">Question?</span></h2>

  <span class="sign" style="left:190px;top:3196px">—</span>
  <div class="abs" style="left:243px;top:3200px">How can i pay for my appointment?</div>
  <p class="abs" style="left:243px;top:3232px;width:350px;font-size:11px;line-height:19.5px;font-weight:400;color:#444">Lorem ipsum dolor sit amet, consectetur adipiscing elit, sed do eiusmod tempor incididunt ut labore et dolore magna aliqua. Quis ipsum suspendisse ultrices gravida commodo viverra maec enas accumsan lacus vel facilisis.</p>
  <span class="sign" style="left:188px;top:3322px">+</span>
  <div class="abs" style="left:239px;top:3325px">What can i expect at my first consultation?</div>

  <span class="sign" style="left:645px;top:3194px">+</span>
  <div class="abs" style="left:697px;top:3197px">What can i expect at my first consultation?</div>
  <span class="sign" style="left:645px;top:3232px">+</span>
  <div class="abs" style="left:697px;top:3235px">Do i need a referral?</div>
  <span class="sign" style="left:645px;top:3276px">+</span>
  <div class="abs" style="left:697px;top:3279px">What can i expect at my first consultation?</div>
  <span class="sign" style="left:645px;top:3322px">+</span>
  <div class="abs" style="left:697px;top:3325px">Do i need a referral?</div>

  <a class="btn btn-ghost" style="left:534px;top:3403px;width:132px;height:43px;font-size:11px;border-color:#f5c98a">More Question</a>
</section>

<!-- Footer backdrop & newsletter -->
<div class="abs" style="left:0;top:3649px;width:1200px;height:576px;background:var(--foot)"></div>
<section>
  <div class="abs" style="left:185px;top:3513px;width:833px;height:298px;border-radius:26px;background:var(--blue)"></div>
  <h2 class="abs center head" style="top:3562px;font-size:27px;line-height:35px;color:var(--white);font-weight:400;letter-spacing:1px">To Get Latest News Form Us<br><span style="font-weight:500;letter-spacing:2px">Subscriber Now</span></h2>
  <div class="abs" style="left:328px;top:3667px;width:546px;height:72px;border-radius:40px;background:var(--white)"></div>
  <div class="abs" style="left:375px;top:3696px;font-size:11px;color:#888">user_email@nuvaramail.com</div>
  <a class="btn btn-solid" style="left:698px;top:3675px;width:168px;height:56px;font-size:13px">Subscribe</a>
</section>

<!-- Footer -->
<footer>
  <div class="abs brand" style="left:188px;top:3873px"><i></i>Tallvine</div>
  <p class="abs" style="left:188px;top:3940px;width:255px;font-size:11px;line-height:20px;color:#333">Lorem ipsum dolor sit amet, consectetur adipiscing elit, sed do eiusmod tempor incididunt ut labore et dolore magna aliqua. Ut enim ad minim.</p>
  <div class="abs" style="left:188px;top:4060px;display:flex;gap:22px">
    <span style="width:12px;height:12px;border-radius:50%;background:var(--ink)"></span>
    <span style="width:12px;height:12px;border-radius:50%;background:var(--ink)"></span>
    <span style="width:12px;height:12px;border-radius:50%;background:var(--ink)"></span>
    <span style="width:12px;height:12px;border-radius:50%;background:var(--ink)"></span>
  </div>

  <div class="abs foot-col" style="left:543px;top:3879px;width:150px;height:200px">
    <h5>About Agency</h5>
    <a style="top:62px">Home</a><a style="top:101px">About</a><a style="top:139px">Services</a><a style="top:178px">Contacts</a>
  </div>
  <div class="abs foot-col" style="left:711px;top:3879px;width:150px;height:200px">
    <h5>Quick Link</h5>
    <a style="top:62px">Home</a><a style="top:101px">About</a><a style="top:139px">Services</a><a style="top:178px">Contacts</a>
  </div>
  <div class="abs foot-col" style="left:864px;top:3879px;width:160px">
    <h5>Contact Us</h5>
    <p style="margin-top:38px;font-size:11px;line-height:19px">Lorem ipsum dolor sit amet consecte.</p>
  </div>
  <svg class="abs" style="left:864px;top:4002px" width="16" height="16" viewBox="0 0 16 16" fill="none" stroke="#333" stroke-width="1.2"><path d="M3 1.5l3 3-1.6 1.8a9 9 0 0 0 5.3 5.3L11.5 10l3 3-2 2C6 15 1 10 1 3.5z"/></svg>
  <div class="abs" style="left:897px;top:4002px;font-size:12px">(01) 555-0147</div>
  <svg class="abs" style="left:864px;top:4038px" width="16" height="13" viewBox="0 0 16 13" fill="none" stroke="#333" stroke-width="1.2"><rect x="1" y="1" width="14" height="11"/><path d="M1 1l7 6 7-6"/></svg>
  <div class="abs" style="left:897px;top:4037px;font-size:12px">lorem@nuvaramail.com</div>

  <div class="abs" style="left:188px;top:4117px;width:832px;height:1px;background:#dadada"></div>
  <p class="abs center" style="top:4155px;font-size:11px;color:#333">Copyright © 2021 Tallvine. Limited. All rights reserved</p>
</footer>

</body>
</html>
```